Design a Bold Tradeshow Backdrop for a Sustainable Cleaning Technology

We need a professional, high-impact 10' × 8' tradeshow backdrop for Vornelle®, a commercial cleaning technology company. 143.75" x 90" high and needs bleeds in the 143.75" direction for printing but the graphic area is 10' wide.

Our first event will have an audience that includes K–12 school administrators, facility managers, business officials, and custodial decision-makers. However, this backdrop will be used at multiple future trade shows across different commercial and institutional markets.

The design therefore needs to be universal rather than specifically education- or school-themed.

Our goal is to stop attendees as they walk past the booth and immediately communicate a simple message:

Safer and more sustainable cleaning can also cost substantially less than conventional cleaning chemicals.

We want the design to feel modern, innovative, clean, sustainable, credible, commercial, and premium. It should resonate with K–12 decision-makers while being equally appropriate at events serving commercial facilities, healthcare, hospitality, government, property management, transportation, and other institutional markets.

It should NOT look like a traditional janitorial supply advertisement and should not be overly busy.

The most important messages need to be understandable from approximately 10–20 feet away.

Required Messaging

The primary headline should be:

SUSTAINABLE CLEANING
DOES NOT HAVE TO BE EXPENSIVE.

Three major value propositions should be prominently displayed:

FREE
Cleaning Chemical Analysis
See how much you can save.

SAVE UP TO 60% or More
on Cleaning Chemical Costs

AS LITTLE AS $0.27/GALLON

We would also like a strong secondary message incorporated into the design:

SMARTER CLEANING.
High Performance. Low Cost. Safer.

Visual Direction — Important

Rather than showing a K–12 school hallway or other environment that limits the backdrop to the education market, we want a sophisticated, universal commercial or institutional environment.

This could be a bright, contemporary commercial facility, lobby, corridor, office environment, public building, or other premium architectural space that could reasonably represent many different types of facilities.

The environment should communicate:

Cleanliness • Safety • Sustainability • Professionalism • Efficiency • High Performance

We want someone from a school, hospital, hotel, office building, airport, government facility, or other commercial property to be able to look at the backdrop and relate the imagery to their own facility.

Please avoid imagery that makes the backdrop industry-specific.

We also want to avoid clichéd environmental imagery. The design does not need to be covered in leaves, trees, water droplets, recycling symbols, or other obvious "green" graphics to communicate sustainability. We prefer a sophisticated commercial interpretation of sustainability.

Color & Brand Direction

We want the overall color palette to stay primarily within:

Blues — consistent with our corporate identity

Greens — to reinforce sustainability, safety, efficiency, and environmental responsibility

White — strongly encouraged for clean space, contrast, and an open contemporary appearance

Black — should be limited primarily to text where necessary for readability

Please avoid making black a major background or dominant design color.

We want the finished display to have a bright, clean, sophisticated, sustainable look and feel rather than a dark or industrial appearance.

The design should use significant negative space and a strong visual hierarchy.

Less is more.

We prefer a few large, powerful messages that can be understood quickly rather than numerous small bullet points, paragraphs, or icons.

Creative Freedom

The attached concept image is provided to communicate our general direction and messaging only.

It does not need to be copied.

We are specifically running this contest because we want designers to improve upon our initial concept and show us different creative approaches to presenting the Vornelle value proposition.

We are open to creative interpretations of the commercial environment, composition, typography, use of negative space, and how the three major financial benefits are presented.

The finished design should feel like an innovative commercial technology brand, not simply another cleaning chemical company.

Corporate Logo — Very Important

We are attaching our official Vornelle® corporate logo for use in the design.

DO NOT redraw, recreate, modify, stylize, reinterpret, trace, or AI-generate the Vornelle logo.

The supplied corporate logo must be inserted directly into the artwork exactly as provided, maintaining its original proportions, colors, typography, trademark elements, and graphic design.

The logo should generally appear in the upper-left area of the backdrop but should not overwhelm the primary marketing message.

Printer Template & Graphic Sizing

We are also attaching the printer's official graphic template and instructions for the 8' × 8' tension-fabric display.

Designers should create their artwork using these supplied specifications so the winning design can be transferred directly into production.

The printer requires that the original document size not be changed, artwork be created on the designated design layer or a new layer, images be embedded, text be converted to outlines, and the finished production artwork be supplied as a PDF.

Please pay particular attention to the bleed area, finished size, and safe artwork area when positioning important text, graphics, and the corporate logo.

Physical Booth Context

The backdrop will sit behind an 8' tradeshow table.

The complete booth will also contain:

A blue stretch tablecloth with the Vornelle corporate logo
BrevoMax and Vornelle product containers and samples on the table
An HulaDrent chemical mixing/dilution station displayed on an elevated stand to the left
A television/monitor to the right demonstrating our online ROI cost-savings calculator

Because these other booth elements will explain our products and technology in greater detail, the backdrop should NOT attempt to explain everything we do.

Its primary purpose is to stop traffic, establish the Vornelle brand, and communicate our core economic and sustainability value proposition.

Final Deliverables

The winning designer must provide artwork properly sized and positioned using our supplied 8' × 8' tension-fabric display template.

Final files should include:

Print-ready, high-resolution PDF
Editable source/vector artwork
All images embedded
Fonts converted to outlines
Artwork correctly positioned within the supplied printer template
Original Vornelle corporate logo incorporated without modification
The 3–5 Second Test

This is perhaps the most important requirement.

Someone walking down a tradeshow aisle should be able to look at the backdrop for 3–5 seconds and understand:

Vornelle offers safer, sustainable, high-performance commercial cleaning — at a lower cost.

The three offers we particularly want them to remember are:

FREE CHEMICAL ANALYSIS

SAVE UP TO 60%

AS LITTLE AS $0.27/GALLON

The overall takeaway should be:

Sustainable cleaning does not have to cost more.

We want the winning design to make that message immediately understandable, credible, and memorable.

Colors
0054AA
0677BA
7BADD7
CADEEF
E8F1F8
0094D4
00A9DD
6FCCEA
C7EBF8
E9F6FB
00AB8E
00BBA5
67D7C9
C6EFE9
E9F9F6
59FF00
82FF00
B8FF75
E3FFCB
F4FFEA

```html
<!DOCTYPE html>
<html lang="en">
<head>
<meta charset="utf-8">
<title>Vornelle Tradeshow Backdrop</title>
<link rel="stylesheet" href="https://fonts.googleapis.com/css2?family=Montserrat:wght@500;600;700;800;900&display=swap">
<style>
  :root {
    --navy: #1d3f7e;
    --navy-deep: #1a2550;
    --blue: #2f74c0;
    --green: #6e9e3c;
    --ink: #1a1a1a;
    --white: #ffffff;
    --stage: #c9c9c9;
    --panel: rgba(255,255,255,0.86);
  }
  * { margin: 0; padding: 0; box-sizing: border-box; }
  html, body { width: 1200px; height: 2317px; overflow: hidden; }
  body {
    background: var(--stage);
    font-family: "Montserrat", Arial, sans-serif;
    position: relative;
  }
  .backdrop {
    position: absolute;
    left: 86px; top: 644px;
    width: 1028px; height: 1028px;
    background: var(--white);
    overflow: hidden;
    box-shadow: 4px 6px 10px rgba(0,0,0,0.25);
  }
  .backdrop span, .backdrop svg { position: absolute; }
  .line { line-height: 1; white-space: nowrap; }

  .lobby-photo {
    position: absolute;
    left: 0; top: 520px; width: 1028px; height: 508px;
    background:
      linear-gradient(180deg, rgba(255,255,255,1) 0%, rgba(255,255,255,0) 22%),
      radial-gradient(ellipse at 55% 35%, #f4f4f4 0%, #dcdcdc 45%, #c9c9c9 100%),
      #d6d6d6;
  }

  .brand-name {
    left: 89px; top: 105px;
    font-weight: 700; font-size: 60px; color: var(--ink); letter-spacing: -1px;
  }

  .headline-sustainable { left: 86px; top: 268px; font-weight: 900; font-size: 73px; color: var(--navy); letter-spacing: -1.5px; }
  .headline-cleaning    { left: 84px; top: 334px; font-weight: 900; font-size: 100px; color: var(--green); letter-spacing: -2.5px; }
  .headline-rest        { left: 88px; font-weight: 500; font-size: 57px; color: var(--navy); letter-spacing: -0.5px; }
  .headline-rest.first  { top: 436px; }
  .headline-rest.second { top: 501px; }

  .offers-panel {
    position: absolute; left: 711px; top: 370px;
    width: 261px; height: 510px;
    background: var(--panel);
    border-radius: 26px;
  }
  .offer-line { left: 692px; width: 300px; text-align: center; }
  .offer-icon { left: 803px; }

  .free-title   { top: 167px; font-weight: 900; font-size: 66px; color: var(--navy); letter-spacing: -1.5px; }
  .free-sub     { font-weight: 800; font-size: 19px; color: var(--navy); }
  .free-sub.a   { top: 232px; }
  .free-sub.b   { top: 255px; }
  .free-note    { font-weight: 600; font-size: 19px; color: var(--ink); }
  .free-note.a  { top: 277px; }
  .free-note.b  { top: 299px; }

  .save-title   { top: 450px; font-weight: 900; font-size: 64px; color: var(--green); letter-spacing: -1.5px; }
  .save-row     { top: 507px; display: flex; justify-content: center; align-items: center; gap: 6px; }
  .save-upto    { position: static !important; font-weight: 800; font-size: 17px; color: var(--navy); line-height: 16px; text-align: left; }
  .save-pct     { position: static !important; font-weight: 900; font-size: 67px; color: var(--green); letter-spacing: -1px; line-height: 1; }
  .save-sub     { font-weight: 800; font-size: 19px; color: var(--green); }
  .save-sub.a   { top: 575px; }
  .save-sub.b   { top: 597px; }

  .price-lead   { top: 754px; font-weight: 800; font-size: 24px; color: var(--blue); }
  .price-value  { top: 777px; font-weight: 900; font-size: 68px; color: var(--navy); letter-spacing: -1.5px; }
  .price-unit   { top: 847px; font-weight: 600; font-size: 19px; color: var(--blue); }

  .base-band { left: 0; top: 0; }

  .tagline-lead { left: 89px; top: 941px; font-weight: 900; font-size: 39px; color: var(--white); letter-spacing: -1px; }
  .tagline-sub  { left: 544px; top: 951px; font-weight: 600; font-size: 21px; color: var(--white); }
</style>
</head>
<body>
  <main class="backdrop">
    <div class="lobby-photo" role="img" aria-label="Bright modern commercial lobby with marble wall, reception desk and polished floor"></div>

    <span class="line brand-name">Vornelle</span>

    <h1>
      <span class="line headline-sustainable">SUSTAINABLE</span>
      <span class="line headline-cleaning">CLEANING</span>
      <span class="line headline-rest first">DOES NOT HAVE</span>
      <span class="line headline-rest second">TO BE EXPENSIVE.</span>
    </h1>

    <div class="offers-panel"></div>

    <svg class="offer-icon" style="top:80px" width="78" height="78" viewBox="0 0 76 76" aria-hidden="true">
      <circle cx="38" cy="38" r="38" fill="var(--navy)"/>
      <path d="M31 20h14M34 20v14l-12 20a3 3 0 0 0 3 4h26a3 3 0 0 0 3-4L42 34V20" fill="none" stroke="#fff" stroke-width="4" stroke-linejoin="round" stroke-linecap="round"/>
      <circle cx="32" cy="50" r="3" fill="#fff"/><circle cx="42" cy="48" r="2.5" fill="#fff"/><circle cx="38" cy="42" r="2" fill="#fff"/>
    </svg>
    <span class="line offer-line free-title">FREE</span>
    <span class="line offer-line free-sub a">CLEANING</span>
    <span class="line offer-line free-sub b">CHEMICAL ANALYSIS</span>
    <span class="line offer-line free-note a">See how much you</span>
    <span class="line offer-line free-note b">can save.</span>

    <svg class="offer-icon" style="top:363px" width="78" height="78" viewBox="0 0 76 76" aria-hidden="true">
      <circle cx="38" cy="38" r="38" fill="var(--green)"/>
      <path d="M18 50l14-14 8 8 16-16M44 26h14v14" fill="none" stroke="#fff" stroke-width="6" stroke-linecap="round" stroke-linejoin="round"/>
    </svg>
    <span class="line offer-line save-title">SAVE</span>
    <span class="offer-line save-row"><span class="save-upto">UP<br>TO</span><span class="save-pct">60%</span></span>
    <span class="line offer-line save-sub a">ON CLEANING</span>
    <span class="line offer-line save-sub b">CHEMICAL COSTS</span>

    <svg class="offer-icon" style="top:659px" width="78" height="78" viewBox="0 0 76 76" aria-hidden="true">
      <circle cx="38" cy="38" r="38" fill="var(--blue)"/>
      <text x="38" y="55" text-anchor="middle" font-family="Montserrat, sans-serif" font-weight="900" font-size="48" fill="#fff">$</text>
    </svg>
    <span class="line offer-line price-lead">AS LITTLE AS</span>
    <span class="line offer-line price-value">$0.27</span>
    <span class="line offer-line price-unit">/GALLON</span>

    <svg class="base-band" width="1028" height="1028" viewBox="0 0 1028 1028" aria-hidden="true">
      <defs>
        <linearGradient id="band-fill" x1="0" y1="0" x2="1" y2="0">
          <stop offset="0" stop-color="var(--navy-deep)"/>
          <stop offset="0.5" stop-color="#1f3f7a"/>
          <stop offset="1" stop-color="var(--navy-deep)"/>
        </linearGradient>
      </defs>
      <path d="M0 795 C120 860 300 900 520 905 C700 908 900 880 1028 880 V1028 H0 Z" fill="var(--green)"/>
      <path d="M0 845 C180 895 380 910 560 905 C760 898 900 890 1028 905 V1028 H0 Z" fill="var(--blue)"/>
      <path d="M0 850 C180 900 380 915 560 912 C760 908 880 920 1028 960 V1028 H0 Z" fill="url(#band-fill)"/>
    </svg>

    <p>
      <span class="line tagline-lead">SMARTER CLEANING.</span>
      <span class="line tagline-sub">High Performance. Low Cost. Safer.</span>
    </p>
  </main>
</body>
</html>
```